Business Card Redesign

We would like to redesign our existing business cards.
The new design shall look:
ELEGANT, LUXURY, PROFESSIONAL
Reference:
YOU CAN VISIT WWW.LUMEN-RIVET.HK FOR BETTER UNDERSTANDING OF COMPANY STRATEGY AND POSITION
Additional:
CHOSEN CANDIDATE SHALL PROVIDE THE INSTRUCTION OF PRINTING IF ANY THERMAL COVERAGE OR ANY ADDITION IS OFFERED
Industry/Entity Type
Business

```html
<!DOCTYPE html>
<html lang="en">
<head>
<meta charset="utf-8">
<title>Lumen &amp; Rivet Limited – Business Card</title>
<link rel="stylesheet" href="https://fonts.googleapis.com/css2?family=EB+Garamond:wght@400;500&family=PT+Sans:wght@400;700&family=Noto+Sans+TC:wght@400;500&display=swap">
<style>
  :root {
    --page: #e9e9ee;
    --silver-light: #f2f2f2;
    --silver-mid: #c9c9c9;
    --silver-dark: #a7a7a7;
    --gold: #e8a713;
    --blue: #0b5aa0;
    --navy: #0f3f7a;
    --ink: #2b2b2b;
    --white: #ffffff;
  }
  * { box-sizing: border-box; margin: 0; padding: 0; }
  html, body { width: 1200px; height: 987px; overflow: hidden; }
  body {
    background: var(--page);
    font-family: "PT Sans", Arial, sans-serif;
    color: var(--ink);
    position: relative;
  }
  .icon-defs { position: absolute; width: 0; height: 0; }

  .card {
    position: absolute;
    left: 280px;
    width: 640px;
    height: 384px;
    border-radius: 22px;
    overflow: hidden;
    box-shadow: 0 10px 28px rgba(0,0,0,.18);
    background: var(--gold);
  }
  .card--english { top: 64px; }
  .card--chinese { top: 520px; }

  .card__metal {
    position: absolute; left: 0; top: 0; width: 100%; height: 150px;
    background:
      repeating-linear-gradient(90deg, rgba(255,255,255,.18) 0 2px, rgba(0,0,0,.04) 2px 5px),
      linear-gradient(100deg, var(--silver-dark) 0%, var(--silver-light) 40%, var(--silver-mid) 70%, var(--silver-light) 100%);
  }
  .card__band {
    position: absolute; left: 0; bottom: 0; width: 100%; height: 66px;
    background: var(--blue);
  }

  .brand {
    position: absolute; top: 60px; left: 0; width: 100%;
    display: flex; align-items: center; justify-content: center; gap: 12px;
  }
  .brand__dot {
    width: 26px; height: 26px; border-radius: 50%; background: var(--navy);
  }
  .brand__name {
    font-weight: 700; font-size: 28px; letter-spacing: 1px; color: var(--navy);
  }

  .office {
    position: absolute; top: 172px; left: 30px; width: 270px;
    text-align: right; font-size: 16px; line-height: 1.3;
  }
  .office__title { font-weight: 700; font-size: 18px; }
  .card--chinese .office { font-family: "Noto Sans TC", sans-serif; font-size: 16px; line-height: 1.5; }
  .card--chinese .office__title { font-weight: 500; }

  .divider {
    position: absolute; left: 318px; top: 176px; width: 1px; height: 120px;
    background: rgba(255,255,255,.75);
  }

  .contacts {
    position: absolute; top: 174px; left: 338px; list-style: none;
    font-size: 18px; line-height: 1.55;
  }
  .contacts li { display: flex; align-items: center; gap: 8px; }
  .contacts svg { width: 15px; height: 15px; fill: var(--ink); flex: none; }

  .person {
    position: absolute; left: 40px; bottom: 16px;
    font-family: "EB Garamond", Georgia, serif; color: var(--white);
    font-size: 32px; line-height: 1;
  }
  .person__role { font-size: 21px; color: var(--gold); }
  .card--chinese .person { font-family: "Noto Sans TC", sans-serif; font-size: 28px; }
  .card--chinese .person__role { font-size: 19px; }
</style>
</head>
<body>

<svg class="icon-defs" aria-hidden="true">
  <symbol id="icon-mobile" viewBox="0 0 16 16"><rect x="4" y="1" width="8" height="14" rx="1.5"/><rect x="5.5" y="3" width="5" height="7" fill="#e8a713"/></symbol>
  <symbol id="icon-phone" viewBox="0 0 16 16"><circle cx="8" cy="8" r="7.5"/><path d="M5 4l2 2-1 1.2c.6 1.3 1.5 2.2 2.8 2.8L10 9l2 2-1.3 1.5C7 12 4 9 3.5 5.3z" fill="#e8a713"/></symbol>
  <symbol id="icon-fax" viewBox="0 0 16 16"><rect x="4" y="2" width="8" height="5"/><rect x="1" y="7" width="14" height="7" rx="1.5"/></symbol>
  <symbol id="icon-mail" viewBox="0 0 16 16"><rect x="1" y="3.5" width="14" height="9" rx="1"/><path d="M1.5 4l6.5 5 6.5-5" stroke="#e8a713" stroke-width="1.3" fill="none"/></symbol>
  <symbol id="icon-web" viewBox="0 0 16 16"><circle cx="8" cy="8" r="7"/><path d="M1 8h14M8 1c-3 3-3 11 0 14M8 1c3 3 3 11 0 14" stroke="#e8a713" stroke-width="1" fill="none"/></symbol>
</svg>

<section class="card card--english" aria-label="Business card, English side">
  <div class="card__metal"></div>
  <div class="card__band"></div>
  <div class="brand"><span class="brand__dot"></span><span class="brand__name">LUMEN &amp; RIVET LIMITED</span></div>
  <div class="office">
    <p class="office__title">Headquarters (Hong Kong)</p>
    <p>Rm. 2304B, 23/F, Harbourlight Centre</p>
    <p>18 Lantern Road, Central</p>
    <p>Hong Kong</p>
  </div>
  <div class="divider"></div>
  <ul class="contacts">
    <li><svg><use href="#icon-mobile"/></svg>(852) 6140 3827</li>
    <li><svg><use href="#icon-phone"/></svg>(852) 2730-4418</li>
    <li><svg><use href="#icon-fax"/></svg>(852) 2730-4412</li>
    <li><svg><use href="#icon-mail"/></svg>elise@lumen-rivet.hk</li>
    <li><svg><use href="#icon-web"/></svg>www.lumen-rivet.hk</li>
  </ul>
  <p class="person">Elise Varn, <span class="person__role">PR Consultant</span></p>
</section>

<section class="card card--chinese" lang="zh-Hant" aria-label="Business card, Chinese side">
  <div class="card__metal"></div>
  <div class="card__band"></div>
  <div class="brand"><span class="brand__dot"></span><span class="brand__name">LUMEN &amp; RIVET LIMITED</span></div>
  <div class="office">
    <p class="office__title">香港總部</p>
    <p>香港中環燈籠道 18 號</p>
    <p>灣光中心 23 樓 2304B</p>
  </div>
  <div class="divider"></div>
  <ul class="contacts">
    <li><svg><use href="#icon-mobile"/></svg>(852) 6140 3827</li>
    <li><svg><use href="#icon-phone"/></svg>(852) 2730-4418</li>
    <li><svg><use href="#icon-fax"/></svg>(852) 2730-4412</li>
    <li><svg><use href="#icon-mail"/></svg>elise@lumen-rivet.hk</li>
    <li><svg><use href="#icon-web"/></svg>www.lumen-rivet.hk</li>
  </ul>
  <p class="person">溫麗思, <span class="person__role">公關顧問</span></p>
</section>

</body>
</html>
```